New (old) Business Card Design Project

I would like to purchase a customized version of a design you have previously submitted - https://www.artmarketly.example/design/7305126

I like the card above, and would like to use the same design, jus with my business name, HARLOWAY ASSET ADVISORS. I like the colors in the card above, as well as the font. The other side will have my name, company name, address, phone, email, website, plus disclosure text I will provide.

Target Market(s)

wealthy families

Industry/Entity Type

Financial Services

Contact Information for Business Card

logo on one side, on other my name, company, address, phone, email, website, disclosure language I will provide.

Colors

Designer to choose colors to be used in the design.

Requirements
Must have
• colors: Deep blue and white
Nice to have
• Please see the items I have uploaded, below.
Should not have
• Cheap, tacky look.

```html
<!DOCTYPE html>
<html lang="en">
<head>
<meta charset="utf-8">
<title>Harloway Asset Advisors — Business Card</title>
<link href="https://fonts.googleapis.com/css2?family=Cinzel:wght@400;600&family=Roboto:wght@300;400;700&display=swap" rel="stylesheet">
<style>
  :root {
    --page-bg: #e6e7e8;
    --deep-blue-light: #2a5f80;
    --deep-blue: #1f5274;
    --deep-blue-dark: #1a4565;
    --ink: #1d1d1f;
    --accent-blue: #1d4a6e;
    --paper: #ffffff;
  }
  * { margin: 0; padding: 0; box-sizing: border-box; }
  html, body {
    width: 1200px;
    height: 1200px;
    overflow: hidden;
    background: var(--page-bg);
  }
  .sheet {
    width: 1200px;
    height: 1200px;
    display: flex;
    flex-direction: column;
    align-items: center;
    justify-content: center;
    gap: 80px;
  }
  .card {
    position: relative;
    width: 700px;
    height: 400px;
    box-shadow: 0 6px 18px rgba(0, 0, 0, 0.18);
  }
  .card--brand {
    background: linear-gradient(135deg, var(--deep-blue-light) 0%, var(--deep-blue) 50%, var(--deep-blue-dark) 100%);
    display: flex;
    align-items: center;
    justify-content: center;
  }
  .brand-name {
    font-family: "Cinzel", serif;
    font-weight: 400;
    font-size: 34px;
    letter-spacing: 1px;
    color: var(--paper);
    white-space: nowrap;
  }
  .card--contact {
    background: var(--paper);
  }
  .person {
    position: absolute;
    right: 362px;
    top: 142px;
    text-align: right;
    font-family: "Roboto", sans-serif;
  }
  .person-name {
    font-weight: 700;
    font-size: 27px;
    letter-spacing: 1.5px;
    color: var(--accent-blue);
    line-height: 1.05;
  }
  .person-title {
    font-weight: 400;
    font-size: 15px;
    letter-spacing: 1px;
    color: var(--ink);
    margin-top: 2px;
  }
  .divider {
    position: absolute;
    left: 352px;
    top: 160px;
    width: 1.5px;
    height: 150px;
    background: var(--ink);
  }
  .details {
    position: absolute;
    left: 368px;
    top: 214px;
    font-family: "Roboto", sans-serif;
    font-weight: 300;
    font-size: 15px;
    line-height: 1.3;
    color: var(--ink);
  }
  .details-company {
    font-family: "Cinzel", serif;
    font-weight: 600;
    font-size: 15.5px;
    letter-spacing: 0.5px;
    margin-bottom: 2px;
  }
  .details-label { display: inline-block; width: 56px; }
  .details-web {
    font-weight: 400;
    color: var(--accent-blue);
  }
</style>
</head>
<body>
  <main class="sheet">
    <section class="card card--brand" aria-label="Card front">
      <h1 class="brand-name">HARLOWAY ASSET ADVISORS</h1>
    </section>

    <section class="card card--contact" aria-label="Card back">
      <div class="person">
        <p class="person-name">CALLUM REYNARD</p>
        <p class="person-title">MANAGING DIRECTOR</p>
      </div>
      <div class="divider"></div>
      <div class="details">
        <p class="details-company">HARLOWAY ASSET ADVISORS</p>
        <p>121, XXXX XXXX XXXX XXXX</p>
        <p>PHONE: XXXXXXXXX</p>
        <p><span class="details-label">EMAIL</span>: info@xxxxxxxx.com</p>
        <p class="details-web">www.xxxxxxxx.com</p>
      </div>
    </section>
  </main>
</body>
</html>
```